I need a label with logo to go on jars of honey.
Label size 70mm x 70mm
The front label should say :
The Kestrel Honey Co. (logo)
Torvale Honey
400g
The back label:
Would have nutritional information
And our address
You can see from the uploaded files the styles I prefer, I have uploaded a photo of the honey product too. The background of the logo doesn't have to be white. I would like to develop a color scheme that would look nice against the color of the honey.
The Kestrel Honey Co. / The Kestrel Honey Company

```html
<!DOCTYPE html>
<html lang="en">
<head>
<meta charset="UTF-8">
<title>Torvale Honey – Jar Label</title>
<link rel="stylesheet" href="https://fonts.googleapis.com/css2?family=Anton&family=Archivo+Black&family=Kaushan+Script&display=swap">
<style>
  :root {
    --page-bg: #e9e9e9;
    --label-cream: #f2dca0;
    --label-cream-light: #f6e6b8;
    --label-gold: #e9b24a;
    --band-orange: #e79a2c;
    --band-orange-deep: #d9801c;
    --honey-light: #f7d77a;
    --honey-mid: #eeb548;
    --honey-deep: #d8892a;
    --ink-dark: #2e2d2f;
    --brand-red: #c44a2a;
    --script-red: #c9452a;
    --outline-white: #fff8ee;
  }
  * { box-sizing: border-box; margin: 0; padding: 0; }
  html, body {
    width: 1200px;
    height: 960px;
    overflow: hidden;
    background: var(--page-bg);
  }
  .canvas {
    position: relative;
    width: 1200px;
    height: 960px;
    background: var(--page-bg);
  }
  .label {
    position: absolute;
    left: 292px;
    top: 105px;
    width: 615px;
    height: 750px;
    overflow: hidden;
    background: linear-gradient(180deg, var(--label-cream) 0%, var(--label-cream-light) 45%, var(--label-cream) 100%);
  }
  .label__top-band {
    position: absolute;
    left: 0; top: 0;
    width: 100%;
    height: 82px;
    background: linear-gradient(180deg, var(--band-orange-deep) 0%, var(--band-orange) 55%, var(--label-gold) 100%);
  }
  .label__top-rule {
    position: absolute;
    left: 0; top: 40px;
    width: 100%;
    height: 10px;
    background: var(--honey-mid);
    opacity: .7;
  }
  .art { position: absolute; }
  .art--drip-right {
    left: 330px; top: 0;
    width: 285px; height: 175px;
    border-radius: 0 0 40px 120px;
    background: radial-gradient(ellipse at 40% 40%, var(--honey-light) 0%, var(--honey-mid) 70%, var(--honey-deep) 100%);
  }
  .art--drip-centre {
    left: 120px; top: 0;
    width: 95px; height: 60px;
    border-radius: 0 0 45px 45px;
    background: linear-gradient(180deg, var(--honey-mid), var(--honey-deep));
  }
  .art--dipper {
    left: 0; top: 30px;
    width: 140px; height: 185px;
    border-radius: 0 60px 50px 0;
    background: linear-gradient(160deg, var(--honey-light) 0%, var(--honey-mid) 60%, var(--label-gold) 100%);
  }
  .art--comb-pattern {
    left: 0; top: 490px;
    width: 100%; height: 150px;
    background: linear-gradient(180deg, rgba(233,178,74,0) 0%, rgba(233,150,70,.35) 60%, rgba(233,150,70,.5) 100%);
  }
  .art--honeycomb {
    left: 0; top: 420px;
    width: 195px; height: 330px;
    border-radius: 0 90px 40px 0;
    background: radial-gradient(ellipse at 35% 45%, var(--honey-light) 0%, var(--honey-mid) 65%, var(--label-gold) 100%);
  }
  .label__bottom-band {
    position: absolute;
    left: 0; bottom: 0;
    width: 100%;
    height: 110px;
    background: linear-gradient(180deg, var(--band-orange) 0%, var(--band-orange-deep) 100%);
  }
  .brand {
    position: absolute;
    left: 200px; top: 100px;
    width: 180px;
    text-align: center;
    font-family: "Archivo Black", sans-serif;
    font-size: 22px;
    line-height: 1.15;
    color: var(--brand-red);
  }
  .brand__rule {
    position: absolute;
    top: 127px;
    height: 3px;
    background: var(--brand-red);
  }
  .brand__rule--left { left: 150px; width: 55px; }
  .brand__rule--right { left: 375px; width: 55px; }
  .product-name {
    position: absolute;
    left: 23px; top: 200px;
    width: 550px;
    height: 250px;
    overflow: visible;
  }
  .product-name text {
    font-family: "Anton", sans-serif;
    font-size: 244px;
    font-weight: 400;
    fill: var(--ink-dark);
  }
  .product-type {
    position: absolute;
    left: 235px; top: 460px;
    font-family: "Kaushan Script", cursive;
    font-size: 122px;
    line-height: 1;
    color: var(--script-red);
    -webkit-text-stroke: 6px var(--outline-white);
    paint-order: stroke fill;
    transform: rotate(-16deg);
    transform-origin: left center;
  }
  .net-weight {
    position: absolute;
    left: 206px; top: 662px;
    font-family: "Archivo Black", sans-serif;
    font-size: 52px;
    line-height: 1;
    color: var(--ink-dark);
  }
</style>
</head>
<body>
  <main class="canvas">
    <section class="label" aria-label="Torvale Honey jar label">
      <div class="label__top-band"></div>
      <div class="label__top-rule"></div>
      <div class="art art--drip-centre" role="img" aria-label="Illustration of honey dripping from the top edge"></div>
      <div class="art art--drip-right" role="img" aria-label="Illustration of a large honey drip flowing down from the top"></div>
      <div class="art art--dipper" role="img" aria-label="Illustration of a honey dipper with a bee resting on it"></div>
      <div class="art art--comb-pattern" role="img" aria-label="Decorative honeycomb hexagon pattern"></div>
      <div class="label__bottom-band"></div>
      <div class="art art--honeycomb" role="img" aria-label="Illustration of golden honeycomb pieces"></div>

      <span class="brand__rule brand__rule--left"></span>
      <p class="brand">The Kestrel<br>Honey Co.</p>
      <span class="brand__rule brand__rule--right"></span>

      <svg class="product-name" viewBox="0 0 550 250" role="heading" aria-level="1" aria-label="Torvale">
        <text x="0" y="237" textLength="548" lengthAdjust="spacingAndGlyphs">TORVALE</text>
      </svg>
      <p class="product-type">Honey</p>
      <p class="net-weight">400G</p>
    </section>
  </main>
</body>
</html>
```